Certificates with Watermark Images

We are looking for a design of One page Certificates with Watermark (background) images where text will be printed over it .
Graphics design is required to reflect the flowing categories:
IPTV (Internet Protocol TV)
VoD (Video on Demand)
Satellite Receiver
Graphics design images for all three categories must be provided to maintain the same them .
Thank you and good luck.
Industry/Entity Type
Internet
Requirements
Must have
- Graphics design images for all three categories must be provided to maintain the same them

```html
<!DOCTYPE html>
<html lang="en">
<head>
<meta charset="UTF-8">
<title>Certificate of Achievement</title>
<link rel="stylesheet" href="https://fonts.googleapis.com/css2?family=UnifrakturMaguntia&family=EB+Garamond:wght@400;600&display=swap">
<style>
  :root {
    --paper-light: #fdfdf8;
    --paper: #f3f0e0;
    --paper-edge: #ece8d2;
    --frame: #a3a3a3;
    --frame-dots: #b4b4b4;
    --ink: #7d7d7d;
    --ink-strong: #6e6e6e;
    --title: #8a8a8a;
    --title-shadow: #4f4f4f;
    --rule: #b9b9b9;
    --art: #c9c9c6;
  }
  html, body {
    margin: 0;
    padding: 0;
    width: 1200px;
    height: 849px;
    overflow: hidden;
    background: var(--paper-edge);
  }
  .certificate {
    position: relative;
    width: 1200px;
    height: 849px;
    background: radial-gradient(ellipse 60% 55% at 50% 45%, var(--paper-light) 0%, var(--paper) 75%, var(--paper-edge) 100%);
    font-family: "EB Garamond", "Times New Roman", serif;
    color: var(--ink);
  }
  .frame-outer {
    position: absolute;
    inset: 22px 24px;
    border: 2px solid var(--frame);
  }
  .frame-dots {
    position: absolute;
    inset: 30px 32px;
    border: 3px dotted var(--frame-dots);
  }
  .frame-inner {
    position: absolute;
    inset: 42px 44px;
    border: 2px solid var(--frame);
  }
  .title {
    position: absolute;
    left: 0;
    top: 0;
  }
  .title text {
    font-family: "UnifrakturMaguntia", "Times New Roman", serif;
    font-size: 74px;
    fill: var(--title);
  }
  .title .title-shadow {
    fill: var(--title-shadow);
  }
  .lead {
    position: absolute;
    left: 0;
    width: 1200px;
    text-align: center;
    margin: 0;
    text-transform: uppercase;
  }
  .lead-main {
    top: 253px;
    font-size: 24px;
    letter-spacing: 5px;
  }
  .lead-sub {
    top: 290px;
    font-size: 18px;
    letter-spacing: 3.6px;
  }
  .name-line {
    position: absolute;
    left: 382px;
    top: 434px;
    width: 459px;
    border-top: 2px solid var(--rule);
  }
  .awarded {
    position: absolute;
    left: 0;
    width: 1200px;
    top: 460px;
    margin: 0;
    text-align: center;
    font-size: 19px;
    letter-spacing: 3.6px;
    text-transform: uppercase;
  }
  .awarded .of { text-transform: none; }
  .awarded .date { font-weight: 600; color: var(--ink-strong); }
  .signature-line {
    position: absolute;
    left: 809px;
    top: 697px;
    width: 295px;
    border-top: 1px solid var(--rule);
  }
  .artwork {
    position: absolute;
    border-radius: 30%;
    background: radial-gradient(ellipse at 50% 50%, var(--art) 0%, rgba(201,201,198,0.45) 55%, rgba(201,201,198,0) 100%);
  }
  .art-satellite { left: 983px; top: 55px; width: 158px; height: 102px; }
  .art-film { left: 952px; top: 385px; width: 182px; height: 122px; }
  .art-tv { left: 531px; top: 608px; width: 134px; height: 162px; }
  .art-dish { left: 78px; top: 648px; width: 108px; height: 128px; }
</style>
</head>
<body>
<main class="certificate">
  <div class="frame-outer"></div>
  <div class="frame-dots"></div>
  <div class="frame-inner"></div>

  <svg class="title" width="1200" height="260" viewBox="0 0 1200 260" aria-label="Certificate of Achievement">
    <defs>
      <path id="title-arc" d="M 176 232 Q 605 70 1040 232"/>
      <path id="title-arc-shadow" d="M 179 235 Q 608 73 1043 235"/>
    </defs>
    <text class="title-shadow"><textPath href="#title-arc-shadow" startOffset="50%" text-anchor="middle">Certificate of Achievement</textPath></text>
    <text><textPath href="#title-arc" startOffset="50%" text-anchor="middle">Certificate of Achievement</textPath></text>
  </svg>

  <p class="lead lead-main">This certificate is proudly</p>
  <p class="lead lead-sub">presented for honorable achievement to</p>

  <div class="name-line"></div>

  <p class="awarded">Awarded this day <span class="of">of</span> <span class="date">11th November, 2011</span></p>

  <div class="signature-line"></div>

  <div class="artwork art-satellite" role="img" aria-label="Faint illustration of a satellite"></div>
  <div class="artwork art-film" role="img" aria-label="Faint illustration of a film clapperboard and film reel"></div>
  <div class="artwork art-tv" role="img" aria-label="Faint illustration of a television with an internet symbol on screen"></div>
  <div class="artwork art-dish" role="img" aria-label="Faint illustration of a satellite dish sending signal waves"></div>
</main>
</body>
</html>
```